Billboard design for dentist that sees only children

I own a 12' x 25' digital billboard and I need help with billboard design. My wife is a general dentist that only sees children and is very passionate about giving them a quality dental experience . She has a great reputation in town. Obviously with a billboard there can't be a lot of reading. Maybe something that shows safety, love, experience and children. I am completely open to your ideas. In addition I have other businesses that also need billboard design so this could lead to more work. If you go to Maplecovedental.com under the about section you will find more information about the practice and our phone number. Attached is our logo which could be changed and content specs for the digital billboard. Happy Designing!!

Target Market(s)

Parents with children

Colors

Designer to choose colors to be used in the design.

Requirements
Must have
• Must attract attention and be nice to look at.
Nice to have
• Probably should have children in the picture ..... Maybe
Should not have
• If I see something I don't like I will let you know

```html
<!DOCTYPE html>
<html lang="en">
<head>
<meta charset="utf-8">
<title>Maple Cove Dental – Billboard Revised Design</title>
<link rel="stylesheet" href="https://fonts.googleapis.com/css2?family=Montserrat:wght@600&family=Jost:wght@400&family=Source+Sans+3:wght@400;600;700&display=swap">
<style>
  :root {
    --page-bg: #fdfdfd;
    --title-red: #e8252a;
    --spec-navy: #2f4a6a;
    --spec-grey: #555a60;
    --rule-grey: #6a6a6a;
    --headline-blue: #3b6cb4;
    --headline-navy: #1d3a6c;
    --phone-green: #1f5a4c;
    --brand-teal: #2a7f86;
    --tagline-blue: #3a8fcf;
    --address-grey: #3c3c3c;
    --photo-light: #e9f1f8;
    --photo-mid: #9fc3e2;
    --photo-deep: #3d7fc2;
  }
  * { margin: 0; padding: 0; box-sizing: border-box; }
  html, body { width: 1200px; height: 495px; overflow: hidden; background: var(--page-bg); }
  .sheet { position: relative; width: 1200px; height: 495px; }

  .sheet-title {
    position: absolute; top: 37px; left: 0; width: 100%;
    text-align: center; font-family: "Montserrat", sans-serif; font-weight: 600;
    font-size: 27px; letter-spacing: 0.5px; color: var(--title-red);
  }

  .section-heading {
    position: absolute; font-family: "Jost", sans-serif; font-weight: 400;
    font-size: 24px; color: var(--spec-navy); letter-spacing: 0.3px; white-space: nowrap;
  }
  .dimensions-heading { left: 198px; top: 139px; }
  .specs-heading { left: 641px; top: 173px; }

  .width-rule { position: absolute; left: 94px; top: 185px; width: 475px; height: 1px; background: var(--rule-grey); }
  .width-label {
    position: absolute; left: 300px; top: 174px; padding: 0 8px; background: var(--page-bg);
    font-family: "Jost", sans-serif; font-size: 15px; color: var(--spec-grey); letter-spacing: 1px;
  }
  .height-rule { position: absolute; left: 78px; top: 200px; width: 1px; height: 225px; background: var(--rule-grey); }
  .height-label {
    position: absolute; left: 36px; top: 308px; padding: 3px 0; background: var(--page-bg);
    font-family: "Jost", sans-serif; font-size: 15px; color: var(--spec-grey); letter-spacing: 1px;
  }

  .billboard {
    position: absolute; left: 94px; top: 200px; width: 475px; height: 225px;
    background: #ffffff; border: 1px solid #c9c9c9; overflow: hidden;
    font-family: "Source Sans 3", sans-serif;
  }
  .billboard-photo {
    position: absolute; right: 0; top: 0; width: 320px; height: 100%;
    background:
      radial-gradient(ellipse at 78% 40%, #f2d2b8 0%, rgba(242,210,184,0) 32%),
      radial-gradient(ellipse at 70% 92%, var(--photo-deep) 0%, rgba(61,127,194,0) 45%),
      linear-gradient(90deg, #ffffff 0%, var(--photo-light) 35%, var(--photo-mid) 100%);
  }
  .billboard-fade {
    position: absolute; left: 150px; top: 0; width: 110px; height: 100%;
    background: linear-gradient(90deg, #ffffff 0%, rgba(255,255,255,0) 100%);
  }
  .headline-lead {
    position: absolute; left: 29px; top: 22px; font-size: 21px; font-weight: 600;
    color: var(--headline-blue); white-space: nowrap;
  }
  .headline-main {
    position: absolute; left: 45px; top: 46px; font-size: 21px; font-weight: 700;
    color: var(--headline-navy); white-space: nowrap; letter-spacing: 0.2px;
  }
  .phone {
    position: absolute; left: 36px; top: 103px; display: flex; align-items: center; gap: 8px;
    font-size: 25px; font-weight: 400; color: var(--phone-green); letter-spacing: 0.8px;
  }
  .phone svg { width: 17px; height: 17px; }
  .brand {
    position: absolute; left: 22px; top: 170px; display: flex; align-items: center; gap: 6px;
  }
  .brand-dot { width: 18px; height: 18px; border-radius: 50%; background: var(--brand-teal); }
  .brand-name { font-size: 15px; font-weight: 400; color: var(--brand-teal); white-space: nowrap; }
  .brand-tagline {
    position: absolute; left: 64px; top: 189px; font-size: 7.5px; font-style: italic;
    color: var(--tagline-blue); white-space: nowrap;
  }
  .address {
    position: absolute; left: 22px; top: 210px; font-size: 7px; color: var(--address-grey);
    white-space: nowrap; letter-spacing: 0.2px;
  }

  .spec-list {
    position: absolute; left: 647px; top: 208px; list-style: none;
    font-family: "Jost", sans-serif; font-size: 16px; color: var(--spec-grey);
  }
  .spec-list li { position: relative; padding-left: 18px; height: 24.8px; line-height: 24.8px; white-space: nowrap; }
  .spec-list li::before {
    content: ""; position: absolute; left: 0; top: 10px; width: 5px; height: 5px;
    border-radius: 50%; background: #333;
  }
</style>
</head>
<body>
<main class="sheet">
  <h1 class="sheet-title">REVISED DESIGN (216x456 pixels)</h1>

  <h2 class="section-heading dimensions-heading">DISPLAY DIMENSIONS</h2>
  <div class="width-rule"></div>
  <span class="width-label">456(w)</span>
  <div class="height-rule"></div>
  <span class="height-label">216(h)</span>

  <section class="billboard">
    <div class="billboard-photo" role="img" aria-label="Photo of a smiling young boy in a dental chair with a blue bib, a gloved dentist holding a mirror beside him"></div>
    <div class="billboard-fade"></div>
    <p class="headline-lead">We Love Kids and Know</p>
    <p class="headline-main">HOW TO CARE FOR THEM</p>
    <p class="phone">
      <svg viewBox="0 0 24 24" aria-hidden="true">
        <circle cx="12" cy="12" r="10.5" fill="none" stroke="currentColor" stroke-width="1.6"/>
        <path d="M8.2 6.5l1.8-.4 1.2 2.8-1.3 1c.6 1.4 1.7 2.5 3.1 3.1l1-1.3 2.8 1.2-.4 1.8c-.2.6-.8 1-1.4.9C10.6 15.3 8.7 13.4 8 9.1c-.1-.6.3-1.2.9-1.4z" fill="currentColor"/>
      </svg>
      555 014 2276
    </p>
    <div class="brand">
      <span class="brand-dot"></span>
      <span class="brand-name">Maple Cove Dental</span>
    </div>
    <p class="brand-tagline">general dentistry for children</p>
    <p class="address">ADDRESS: 248 Birchwood Ave</p>
  </section>

  <h2 class="section-heading specs-heading">CONTENT SPECIFICATIONS</h2>
  <ul class="spec-list">
    <li>Composition size: 456 pixels (w) by 216 pixels (h)</li>
    <li>Color mode: RGB</li>
    <li>Resolution: 72 dpi (use high-resolution assets and/or vector graphics)</li>
    <li>Preferred Static file format: PNG</li>
    <li>Supported Static file formats:BMP, JPEG</li>
    <li>Pixel aspect ratio: square pixels</li>
    <li>Preferred Animated file format: AVI (uncompressed)</li>
    <li>Supported Animated file formats: MP4, MOV</li>
    <li>Frames Per Second: 30</li>
  </ul>
</main>
</body>
</html>
```